New south Australia high-end red wine label & logo design

Marvick Estate exports premium south Australian wine to oversea market. We are looking for a professional graphic designer to design a full set of wine label and logo for our new red wine, the label & logo should look 'high-end' & Luxury and attractive. Black & gold color is preferred. I have attached example images to demonstrate the feel that we are looking for. These are just a possible starting point. The expectation is that the label would be professional/polished. I am open to any and all designs that would alter my perception of what will be best!

Target customer -

we need the label to be print-ready.

There will be 3 parts to this design.

Top Cover design with gold text wrapped, the front label and the back label

-Brand name Marvik Estate
-text wine of Australia
-text Cabernet
-Year 2015
-text Sourced from premium Australian wine growing region Merrigal valley

Look and Feel:
• Elegant
• Serious
• Modern/Traditional
• Professional
• Gender Neutral
• Upmarket

--------------Back Label text---------------
Rich and opulent with intense fruit aromas of black berry, liquorice and cassis with hints of dark chocolate and pungent spices. Sumptuous and textured palate with beautifully detailed ripe black fruits flowing seamlessly across the palate. French oak provides a complex harmony and finish of great length, balance and purity.

Produced by Rolk Haven Group International Pty Ltd
27 Fellmore Road,Quandip, South Australia, 5172
14.5 ALC/VOL
Wine of Australia
Approx 8.3 Standard Drinks
Contains Sulphites
750 ML
Please leave the space for Bar Code

Requirements
Must have
• wine name, wine logo, wine type etc (should include all 'must-have the required fields wine lable)
Nice to have
• Desginer's own idea
Should not have
• should not be too playful

```html
<!DOCTYPE html>
<html lang="en">
<head>
<meta charset="utf-8">
<title>Marvik Estate – Cabernet Sauvignon Label</title>
<link href="https://fonts.googleapis.com/css2?family=Cormorant+Garamond:ital,wght@0,500;1,400&family=Montserrat:wght@400&display=swap" rel="stylesheet">
<style>
  :root {
    --canvas: #ffffff;
    --label-black: #0b0b0b;
    --gold: #c9a45a;
    --gold-soft: #b8934a;
    --ivory: #f4f1ea;
    --vintage-red: #c8343f;
    --muted: #9a958c;
  }
  * { margin: 0; padding: 0; box-sizing: border-box; }
  html, body {
    width: 1200px; height: 849px; overflow: hidden;
    background: var(--canvas);
  }
  .sheet { position: relative; width: 1200px; height: 849px; }

  .label {
    position: absolute;
    background: var(--label-black);
    width: 25.3em; height: 20.2em;
    font-size: 16px;
  }
  .label--hero  { left: 93px;  top: 248px; font-size: 21.3px; }
  .label--front { left: 722px; top: 99px; }
  .label--alt   { left: 722px; top: 459px; }

  .label__frame {
    position: absolute; inset: 0.8em;
    border: 0.13em solid var(--gold);
    display: flex; flex-direction: column; align-items: center;
    text-align: center;
  }
  .label__mark {
    width: 2.6em; height: 2.6em; margin-top: 1.9em;
    border: 0.1em solid var(--gold); border-radius: 50%;
  }
  .label__name {
    margin-top: 1.05em;
    font-family: "Cormorant Garamond", Georgia, serif;
    font-weight: 500; font-size: 2.25em; line-height: 1;
    color: var(--ivory); letter-spacing: 0.01em;
  }
  .label__region {
    margin-top: 0.55em;
    font-family: "Montserrat", Arial, sans-serif;
    font-size: 0.8em; letter-spacing: 0.14em;
    color: var(--gold); text-transform: uppercase;
  }
  .label__vintage {
    margin-top: 0.7em;
    font-family: "Montserrat", Arial, sans-serif;
    font-size: 0.85em; letter-spacing: 0.1em;
    color: var(--vintage-red);
  }
  .label__varietal {
    margin-top: 0.45em;
    font-family: "Cormorant Garamond", Georgia, serif;
    font-weight: 500; font-size: 0.95em; letter-spacing: 0.06em;
    color: var(--ivory); text-transform: uppercase;
  }
  .label__source {
    margin-top: 0.35em;
    font-family: "Cormorant Garamond", Georgia, serif;
    font-style: italic; font-size: 0.72em; line-height: 1.6;
    color: var(--muted);
  }
  .label__origin {
    margin-top: 1.1em;
    font-family: "Montserrat", Arial, sans-serif;
    font-size: 0.85em; letter-spacing: 0.12em;
    color: var(--gold); text-transform: uppercase;
  }
</style>
</head>
<body>
<main class="sheet">

  <section class="label label--hero">
    <div class="label__frame">
      <div class="label__mark"></div>
      <h1 class="label__name">MARVIK ESTATE</h1>
      <p class="label__region">Merrigal Valley</p>
      <p class="label__vintage">2015</p>
      <p class="label__varietal">Cabernet Sauvignon</p>
      <p class="label__source">Sourced from premium Australian wine<br>growing region Merrigal Valley</p>
      <p class="label__origin">Wine of Australia</p>
    </div>
  </section>

  <section class="label label--front">
    <div class="label__frame">
      <div class="label__mark"></div>
      <h2 class="label__name">MARVIK ESTATE</h2>
      <p class="label__region">Merrigal Valley</p>
      <p class="label__vintage">2015</p>
      <p class="label__varietal">Cabernet Sauvignon</p>
      <p class="label__source">Sourced from premium Australian wine<br>growing region Merrigal Valley</p>
      <p class="label__origin">Wine of Australia</p>
    </div>
  </section>

  <section class="label label--alt">
    <div class="label__frame">
      <div class="label__mark"></div>
      <h2 class="label__name">MARVIK ESTATE</h2>
      <p class="label__region">Merrigal Valley</p>
      <p class="label__vintage">2015</p>
      <p class="label__varietal">Cabernet Sauvignon</p>
      <p class="label__source">Sourced from premium Australian wine<br>growing region Merrigal Valley</p>
      <p class="label__origin">Wine of Australia</p>
    </div>
  </section>

</main>
</body>
</html>
```